Business card for a Exhibition booth fabrication company

Hi. My company would like to change our corporate name card. We are an events and Exhibition stand builder company. We would like our corporate name card to resonate what we do. I need someone to create something unique that relates to the industry that I am in. The graphic designer should be creative to incorporate the elements of my industry and try to blend in well in the design of the card. Our aim is to ensure that we are unique and our card can look different from our competitors.
Updates

The decision maker was very busy and didnt had time to make this decision

Target Market(s)

Marketing and events manager from all companies

Contact Information for Business Card

The business card should have the following details:
Name
Job Title
Email
Website

Colors

Designer to choose colors to be used in the design.

Requirements
Must have
• The card must be look something that is relevant to the service that I am providing. My website is: www.velmora-buildworks.example
• You can see my website to get more information on what service that I am doing
Nice to have
• On the back of my card, I would like to have a globe image with the incorporation of my company logo. This is to indicate that my services can be done in any part of the world.

```html
<!DOCTYPE html>
<html lang="en">
<head>
<meta charset="utf-8">
<title>Velmora Buildworks – Business Card</title>
<link href="https://fonts.googleapis.com/css2?family=Montserrat:wght@400;500;600;700&display=swap" rel="stylesheet">
<style>
  :root {
    --stage: #1c1c1c;
    --card-dark: #2f2f31;
    --card-light: #ffffff;
    --brand-red: #e3202b;
    --ink-grey: #6b6b6b;
    --band-grey: #8a8a8a;
    --text-light: #f2f2f2;
    --map-tone: #3a3a3c;
  }
  * { box-sizing: border-box; margin: 0; padding: 0; }
  html, body { width: 1200px; height: 880px; overflow: hidden; }
  body {
    background: var(--stage);
    font-family: "Montserrat", sans-serif;
    position: relative;
  }
  .card {
    position: absolute;
    width: 620px;
    height: 360px;
    border-radius: 22px;
    overflow: hidden;
    box-shadow: 0 14px 30px rgba(0,0,0,.45);
  }

  /* Back side */
  .card-back { left: 70px; top: 50px; background: var(--card-dark); }
  .world-map {
    position: absolute; left: 90px; top: 40px; width: 440px; height: 250px;
    border-radius: 40%;
    background: radial-gradient(ellipse at center, var(--map-tone) 0%, rgba(58,58,60,0) 70%);
  }
  .services { position: absolute; left: 0; right: 0; top: 78px; text-align: center; }
  .services-title {
    color: var(--brand-red); font-weight: 700; font-size: 22px;
    letter-spacing: 1px; margin-bottom: 14px;
  }
  .services-list li {
    list-style: none; color: var(--text-light); font-size: 14px;
    line-height: 1.65; font-weight: 500;
  }
  .back-brand {
    position: absolute; right: 34px; bottom: 32px;
    display: flex; align-items: center; gap: 10px;
    color: var(--text-light); font-weight: 700; font-size: 14px; letter-spacing: 2px;
  }
  .brand-dot { width: 16px; height: 16px; border-radius: 50%; background: var(--brand-red); flex: none; }

  /* Front side */
  .card-front { left: 510px; top: 470px; background: var(--card-light); }
  .card-front .decor { position: absolute; inset: 0; }
  .front-brand {
    position: absolute; left: 40px; top: 52px;
    display: flex; align-items: center; gap: 12px;
    color: var(--ink-grey); font-weight: 700; font-size: 22px; letter-spacing: 3px;
  }
  .front-brand .brand-dot { width: 22px; height: 22px; }
  .person { position: absolute; left: 40px; top: 160px; }
  .person-name { color: var(--brand-red); font-weight: 700; font-size: 24px; line-height: 1.2; }
  .person-title { color: var(--ink-grey); font-size: 15px; margin-top: 2px; }
  .contact { position: absolute; left: 40px; top: 244px; }
  .contact li {
    list-style: none; display: flex; align-items: center; gap: 8px;
    color: var(--ink-grey); font-size: 14px; line-height: 1.7;
  }
  .contact svg { width: 13px; height: 13px; fill: var(--brand-red); flex: none; }
  .address {
    position: absolute; right: 34px; top: 214px; width: 200px;
    color: var(--ink-grey); font-size: 14px; line-height: 1.5;
  }
  .website {
    position: absolute; right: 30px; bottom: 12px;
    color: #fff; font-size: 13px; font-weight: 600;
  }
</style>
</head>
<body>

  <section class="card card-back" aria-label="Card back">
    <div class="world-map" role="img" aria-label="Faint world map"></div>
    <div class="services">
      <h2 class="services-title">OUR SERVICES</h2>
      <ul class="services-list">
        <li>Exhibition Booth Fabrication | Outdoor Booth Setup | Interior Design</li>
        <li>Installation and Dismantle | Exhibition Management</li>
        <li>Shell Scheme Display Booth | Custom Stand Design</li>
        <li>Exhibition Furniture and Equipment | Exhibition Project Management</li>
      </ul>
    </div>
    <div class="back-brand"><span class="brand-dot"></span>VELMORA BUILDWORKS</div>
  </section>

  <section class="card card-front" aria-label="Card front">
    <svg class="decor" width="620" height="360" viewBox="0 0 620 360">
      <line x1="230" y1="202" x2="600" y2="202" stroke="var(--brand-red)" stroke-width="1.2"/>
      <path d="M0 318 L330 318 L345 300 L620 300 L620 312 L352 312 L337 330 L0 330 Z" fill="var(--band-grey)"/>
      <path d="M0 330 L337 330 L352 312 L620 312 L620 360 L0 360 Z" fill="var(--brand-red)"/>
    </svg>
    <div class="front-brand"><span class="brand-dot"></span>VELMORA BUILDWORKS</div>
    <div class="person">
      <p class="person-name">Jonas Hale</p>
      <p class="person-title">Director</p>
    </div>
    <ul class="contact">
      <li><svg viewBox="0 0 24 24"><path d="M6.6 10.8a15 15 0 0 0 6.6 6.6l2.2-2.2a1 1 0 0 1 1-.25 11 11 0 0 0 3.6.6 1 1 0 0 1 1 1V20a1 1 0 0 1-1 1A17 17 0 0 1 3 4a1 1 0 0 1 1-1h3.5a1 1 0 0 1 1 1 11 11 0 0 0 .6 3.6 1 1 0 0 1-.25 1z"/></svg>0198 765 432</li>
      <li><svg viewBox="0 0 24 24"><path d="M2 5h20v14H2z M2 5l10 8 10-8" stroke="#fff" stroke-width="1.5"/></svg>info@velmora-buildworks.example</li>
    </ul>
    <p class="address">PO BOX 456, Harbour Lane<br>4th street Avondale</p>
    <p class="website">www.velmora-buildworks.example</p>
  </section>

</body>
</html>
```